2019 Veltrano Quisk Business Wrap

We need a wrap design for a 2019 Veltrano Quisk LX4 double cab, we would like to include our logo ( File uploaded) , phone number 555-072-3916. We would like to include our Lic. # EC27590461. We would also like to include DESIGN BUILD INSTALL, We would like to include our web address brightlanegraphicsco.example. We would also like to have the truck number which is 7 located near the top front fender.

Target Market(s)

Business owners ans Managers

Industry/Entity Type

Signs and Graphics

```html
<!DOCTYPE html>
<html lang="en">
<head>
<meta charset="utf-8">
<title>Brightlane Graphics Co. – Veltrano Quisk Wrap</title>
<link rel="stylesheet" href="https://fonts.googleapis.com/css2?family=Montserrat:wght@600;700;800&display=swap">
<style>
  :root {
    --wrap-black: #0d0f0c;
    --wrap-black-soft: #1a2412;
    --lime: #9bd619;
    --green: #22b24c;
    --white: #ffffff;
    --ink: #0d0f0c;
    --stage: #e6e8e4;
  }
  * { margin: 0; padding: 0; box-sizing: border-box; }
  html, body { width: 1167px; height: 1200px; overflow: hidden; background: var(--stage); }
  body { position: relative; font-family: "Montserrat", Arial, sans-serif; }

  .panel {
    position: absolute;
    background: var(--wrap-black);
    border-radius: 26px;
    overflow: hidden;
  }
  .panel-side { left: 30px; top: 80px; width: 1107px; height: 360px; }
  .panel-rear { left: 200px; top: 705px; width: 767px; height: 250px; border-radius: 14px; }

  .texture {
    position: absolute;
    background: linear-gradient(100deg, rgba(26,36,18,0) 0%, var(--wrap-black-soft) 55%, #2c3d14 100%);
  }
  .panel-side .texture { left: 520px; top: 0; right: 0; bottom: 0; }
  .panel-rear .texture { left: 0; top: 0; right: 0; bottom: 0;
    background: linear-gradient(90deg, #2c3d14 0%, var(--wrap-black-soft) 30%, rgba(26,36,18,0) 60%); }

  .brand-mark {
    position: absolute; border-radius: 50%;
    background: linear-gradient(135deg, var(--lime), var(--green));
  }
  .panel-side .brand-mark { left: 520px; top: 30px; width: 220px; height: 220px; }
  .panel-rear .brand-mark { left: 90px; top: 25px; width: 200px; height: 200px; }

  .brand-name {
    position: absolute; color: var(--white); font-weight: 800; line-height: 1;
    letter-spacing: 0.01em; text-align: right;
  }
  .brand-name .line-main { display: block; }
  .brand-name .line-sub { display: block; letter-spacing: 0.18em; margin-top: 10px; }
  .panel-side .brand-name { right: 620px; top: 168px; }
  .panel-side .brand-name .line-main { font-size: 44px; }
  .panel-side .brand-name .line-sub { font-size: 22px; }
  .panel-rear .brand-name { right: 22px; top: 22px; }
  .panel-rear .brand-name .line-main { font-size: 50px; }
  .panel-rear .brand-name .line-sub { font-size: 20px; }

  .truck-number {
    position: absolute; left: 68px; top: 148px;
    color: var(--green); font-weight: 800; font-size: 20px;
  }
  .license { position: absolute; color: var(--white); font-weight: 700; font-size: 7px; letter-spacing: 0.03em; }
  .panel-side .license { left: 100px; top: 153px; }
  .panel-rear .license { left: 338px; top: 206px; }

  .web-band {
    position: absolute; left: 245px; top: 252px; width: 510px; height: 34px;
    background: linear-gradient(90deg, var(--green), var(--lime));
    border-radius: 4px 0 0 4px;
    color: var(--ink); font-weight: 800; font-size: 14px; letter-spacing: 0.06em;
    display: flex; align-items: center; padding-left: 24px;
  }

  .phone-band {
    position: absolute;
    background: linear-gradient(90deg, var(--green), var(--lime));
    color: var(--ink); font-weight: 800;
    display: flex; align-items: center; gap: 6px;
    border-radius: 18px 0 0 0;
  }
  .phone-band svg { fill: var(--ink); }
  .panel-side .phone-band { left: 790px; top: 105px; width: 320px; height: 42px;
    font-size: 30px; padding-left: 26px; border-radius: 20px 0 0 0; }
  .panel-side .phone-band svg { width: 22px; height: 22px; }

  .panel-rear .contact-band {
    position: absolute; left: 340px; top: 125px; width: 405px; height: 64px;
    background: linear-gradient(90deg, var(--green), var(--lime));
    border-radius: 20px 0 0 0; color: var(--ink);
    display: flex; flex-direction: column; align-items: flex-end; justify-content: center;
    padding-right: 12px;
  }
  .contact-band .phone { display: flex; align-items: center; gap: 6px; font-weight: 800; font-size: 36px; line-height: 1; }
  .contact-band .phone svg { width: 26px; height: 26px; fill: var(--ink); }
  .contact-band .web { font-weight: 800; font-size: 13px; letter-spacing: 0.06em; margin-top: 3px; }

  .services { position: absolute; list-style: none; color: var(--white); font-weight: 800; }
  .services li { display: flex; align-items: center; gap: 6px; }
  .services li::before {
    content: ""; width: 8px; height: 8px; border-radius: 50%; background: var(--lime);
  }
  .panel-side .services { left: 998px; top: 163px; font-size: 15px; line-height: 17px; }
  .panel-rear .services { left: 440px; top: 196px; display: flex; gap: 6px; font-size: 19px; }
</style>
</head>
<body>

  <section class="panel panel-side" aria-label="Side wrap">
    <div class="texture"></div>
    <div class="brand-mark"></div>
    <span class="truck-number">7</span>
    <span class="license">LIC. # EC27590461</span>
    <h1 class="brand-name">
      <span class="line-main">BRIGHTLANE</span>
      <span class="line-sub">GRAPHICS CO.</span>
    </h1>
    <div class="web-band">BRIGHTLANEGRAPHICSCO.EXAMPLE</div>
    <div class="phone-band">
      <svg viewBox="0 0 24 24" aria-hidden="true"><path d="M6.6 10.8a15.1 15.1 0 0 0 6.6 6.6l2.2-2.2a1 1 0 0 1 1-.25 11.4 11.4 0 0 0 3.6.57 1 1 0 0 1 1 1V20a1 1 0 0 1-1 1A17 17 0 0 1 3 4a1 1 0 0 1 1-1h3.5a1 1 0 0 1 1 1c0 1.25.2 2.45.57 3.57a1 1 0 0 1-.25 1z"/></svg>
      555-072-3916
    </div>
    <ul class="services">
      <li>DESIGN</li>
      <li>BUILD</li>
      <li>INSTALL</li>
    </ul>
  </section>

  <section class="panel panel-rear" aria-label="Tailgate wrap">
    <div class="texture"></div>
    <div class="brand-mark"></div>
    <h2 class="brand-name">
      <span class="line-main">BRIGHTLANE</span>
      <span class="line-sub">GRAPHICS CO.</span>
    </h2>
    <div class="contact-band">
      <span class="phone">
        <svg viewBox="0 0 24 24" aria-hidden="true"><path d="M6.6 10.8a15.1 15.1 0 0 0 6.6 6.6l2.2-2.2a1 1 0 0 1 1-.25 11.4 11.4 0 0 0 3.6.57 1 1 0 0 1 1 1V20a1 1 0 0 1-1 1A17 17 0 0 1 3 4a1 1 0 0 1 1-1h3.5a1 1 0 0 1 1 1c0 1.25.2 2.45.57 3.57a1 1 0 0 1-.25 1z"/></svg>
        555-072-3916
      </span>
      <span class="web">BRIGHTLANEGRAPHICSCO.EXAMPLE</span>
    </div>
    <span class="license">LIC. # EC27590461</span>
    <ul class="services">
      <li>DESIGN</li>
      <li>BUILD</li>
      <li>INSTALL</li>
    </ul>
  </section>

</body>
</html>
```